Design für ein Flyer mit Gutschein-Abriss
Zielgruppe
Handgemachte/ handgefertigte Körperpflege- und Kosmetikprodukte, die in kleinen Chargen gefertigt werden (somit wechselnde Produkte, die in bestimmten Mengen verfügbar sind) u.a. Seifen, Rasierseifen, Badezusätze, Gesichtspflege usw.
Die Produkte werden ohne künstliche Zusätze und Konservierungsstoffe hergestellt und erhalten so wenig Allergene-Stoffe wie möglich, zum Teil vegan.
In geringem Umfang werden ebenfalls Zubehör für Körperpflege vermarktet (z.B. Lavastein für Hornhautentfernung etc.).
Die Produkte werden online und im stationären Handel vertrieben.
Ansprechen von möglichst allen Altersgruppen.
Zielgruppe: 'Otto-Normal-Verbraucher', FRAUEN, Eltern (Mutter-Kind), Männer, in geringem Umfang Haustierbesitzer (Hundeshampoos etc.)
Aufgabenstellung
Größe: DinA5
Wir führen folgende Produkte in unserer Manufaktur:
Natürliche handgefertigte Naturseifen (Milchseifen, Kräuterseifen, Aromaseifen, uvm.), Seifentorten, Seifen- und Badecupcakes, handgerollte Badetrüffel, Badesalz, Badeöle, Badeeis, Badefondant, Körper- und Gesichtspflegeprodukte, Badezubehör, Aromatherapie, Dekorationsartikel sowie Geschenkkörbe für Privat- und Firmenkunden.
Die Produkte enthalten natürliche Inhaltsstoffe, zum Teil hochwertige ätherische Öle und sind Paraben- und SLS-frei. Unsere Produkte werden nicht an Tieren getestet. Wir achten bei der Auswahl der Inhaltsstoffe und unseren Lieferanten auf fairen Handel und nachhaltige Produktion.
Des Weiteren führen wir handgemachte Sojawachskerzen, diese sind Paraffin frei und enthalten Sojawachs aus nachhaltiger Produktion.
Der Flyer soll am unteren Rand den Gutschein beinhalten, welches abgeschnitten werden kann (mit 20 % Rabatt gilt für Online und im Laden).
Auf den Flyer sollten auf jeden Fall noch folgende Daten:
Neueröffnung am 05.05.2017
www.quorvalhaus.de
Öffnungszeiten: Freitags von 11:00 bis 18:00 Uhr
Anbei unser Logo so wie ein Link mit Bildern einiger unserer Produkte.
https://www.filetrunk-beispiel.de/sh/x81kqpwe3rd7h2t/ZZZ4mNbVtRKo2LPw8cY37XUhe?dl=0
Wir freuen uns schon auf viele tolle Vorschläge.

```html
<!DOCTYPE html>
<html lang="de">
<head>
<meta charset="utf-8">
<title>Quorval Haus – Neueröffnung</title>
<link href="https://fonts.googleapis.com/css2?family=Amatic+SC:wght@400;700&display=swap" rel="stylesheet">
<style>
  :root{
    --green:#8ee000;
    --green-text:#8cd91c;
    --green-band:#8fe505;
    --grey:#5f5f5f;
    --grey-soft:#6c6c6c;
    --white:#ffffff;
  }
  *{margin:0;padding:0;box-sizing:border-box;}
  html,body{width:846px;height:1200px;overflow:hidden;background:var(--white);}
  body{font-family:"Amatic SC",cursive;}
  .flyer{position:relative;width:846px;height:1200px;overflow:hidden;background:var(--white);}

  .product-photo{
    position:absolute;left:460px;top:20px;width:386px;height:935px;
    background:
      linear-gradient(to right,#ffffff 0%,rgba(255,255,255,0) 22%),
      linear-gradient(to bottom,#ffffff 0%,rgba(255,255,255,0) 6%),
      radial-gradient(ellipse at 70% 30%,#b6f23a 0%,#9be62a 40%,#86d93a 70%,#a7e96a 100%);
  }

  .brand{position:absolute;left:57px;top:52px;}
  .brand-name{font-weight:400;font-size:88px;line-height:1;color:var(--green);letter-spacing:2px;}
  .brand-tagline{font-size:23px;color:var(--grey);margin-top:20px;letter-spacing:.5px;}

  .headline{position:absolute;left:57px;top:348px;font-weight:700;font-size:92px;line-height:1;color:var(--green);}
  .date{position:absolute;left:57px;top:440px;font-weight:700;font-size:96px;line-height:1;color:var(--grey);}

  .intro{position:absolute;left:57px;top:584px;width:370px;font-size:23px;line-height:30px;color:var(--grey-soft);}
  .donation{position:absolute;left:57px;top:738px;width:370px;font-size:23px;line-height:30px;color:var(--green-text);}

  .contact{position:absolute;left:57px;top:830px;font-size:23px;line-height:35px;color:var(--grey-soft);}
  .contact strong{color:var(--green-text);font-weight:700;}
  .contact .sep{margin:0 8px;}

  .coupon{position:absolute;left:0;top:953px;width:846px;height:247px;background:var(--green-band);color:var(--white);}
  .coupon-frame{position:absolute;left:23px;top:23px;width:777px;height:200px;border:4px dashed var(--white);border-right:none;}
  .coupon-leaves{position:absolute;left:700px;top:0;width:146px;height:247px;background:linear-gradient(to right,rgba(255,255,255,0),rgba(255,255,255,.12));}
  .discount{position:absolute;left:58px;top:14px;font-weight:700;font-size:200px;line-height:1;}
  .coupon-info{position:absolute;left:379px;top:62px;}
  .coupon-info p{font-size:34px;line-height:32px;letter-spacing:3px;}
  .coupon-info .code{font-weight:700;font-size:40px;letter-spacing:4px;}
  .coupon-note{margin-top:30px;font-size:16px !important;line-height:16px !important;letter-spacing:2px !important;width:330px;}
  .scissors{position:absolute;left:522px;top:180px;}
</style>
</head>
<body>
<div class="flyer">
  <div class="product-photo" role="img" aria-label="Grüne Sojawachskerze im Glas mit cremiger Wachshaube"></div>

  <header class="brand">
    <div class="brand-name">Quorval Haus</div>
    <div class="brand-tagline">Be natural with Quorval Haus</div>
  </header>

  <h1 class="headline">Neueröffnung</h1>
  <div class="date">05. Mai 2017</div>

  <p class="intro">Natürliche handgefertigte Körper- und Gesichtspflege-produkte, Naturseifen, Sojawachskerzen sowie Geschenkkörbe für Privat- und Firmenkunden.</p>

  <p class="donation">Aus der Rabattaktion spenden wir 5% vom Umsatz an das Kinder-und Jugendhospiz Sonnenwiese.</p>

  <address class="contact" style="font-style:normal">
    <div><strong>Quorval Haus</strong><span class="sep">|</span>Lindenweg 12, 91999 Talbrunn</div>
    <div>Öffnungszeiten: Freitags von 11:00 bis 18:00 Uhr</div>
    <div>info@quorvalhaus.de<span class="sep">|</span><strong>www.quorvalhaus.de</strong></div>
  </address>

  <section class="coupon">
    <div class="coupon-leaves" role="img" aria-label="Gezeichneter Blätterzweig als Verzierung"></div>
    <div class="coupon-frame"></div>
    <div class="discount">-20%</div>
    <div class="coupon-info">
      <p>Rabatt Online und im Laden</p>
      <p>Rabattcode: <span class="code">84B69</span></p>
      <p class="coupon-note">oder einfach ein Foto mit dem Handy machen und vorzeigen.</p>
    </div>
    <svg class="scissors" width="30" height="30" viewBox="0 0 30 30" aria-hidden="true">
      <g fill="none" stroke="#ffffff" stroke-width="2.5" stroke-linecap="round">
        <circle cx="7" cy="22" r="4"/>
        <circle cx="17" cy="25" r="4"/>
        <line x1="10" y1="19" x2="24" y2="4"/>
        <line x1="15" y1="21" x2="12" y2="3"/>
      </g>
    </svg>
  </section>
</div>
</body>
</html>
```